Job advertisement

A graphic job advertisement. It's supposed to be slightly different from the normal ads. Eye-catcher and later the text for the job description.

```html
<!DOCTYPE html>
<html lang="de">
<head>
<meta charset="utf-8">
<title>Power Workers – Stellenanzeige</title>
<link href="https://fonts.googleapis.com/css2?family=Bebas+Neue&family=Oswald:wght@400;500&family=Poppins:wght@500;600;700&family=Roboto:wght@300;400&display=swap" rel="stylesheet">
<style>
  :root {
    --stage: #8f8f8f;
    --red: #c70000;
    --ink: #232323;
    --paper-light: #f7f7f7;
    --paper-edge: #d9d9d9;
    --band-dark: #212121;
    --shelf: #a8602f;
    --shelf-dark: #6b3a1a;
    --yellow: #ffe033;
    --navy: #0b0b2c;
    --navy-deep: #04041a;
    --amber: #f2a531;
    --arrow-grey: #9a9aa8;
    --white: #ffffff;
  }
  * { box-sizing: border-box; margin: 0; padding: 0; }
  html, body { width: 1200px; height: 843px; overflow: hidden; }
  body { background: var(--stage); position: relative; font-family: "Poppins", sans-serif; }

  .poster { position: absolute; top: 69px; width: 512px; height: 724px; overflow: hidden; }

  /* ---------- Light poster ---------- */
  .poster--light {
    left: 66px;
    background: radial-gradient(circle at 45% 58%, var(--white) 0%, var(--paper-light) 35%, var(--paper-edge) 100%);
  }
  .poster--light .kicker,
  .poster--light .headline {
    position: absolute; left: 24px; z-index: 2;
    font-family: "Bebas Neue", sans-serif; line-height: 1; letter-spacing: -1px;
    transform: scaleX(0.9); transform-origin: left top; white-space: nowrap;
  }
  .poster--light .kicker { top: 26px; font-size: 58px; color: var(--ink); }
  .poster--light .headline--power { top: 74px; font-size: 116px; color: var(--red); }
  .poster--light .headline--workers { top: 171px; font-size: 116px; color: var(--ink); }

  .bulb-art {
    position: absolute; left: 352px; top: 40px; width: 138px; height: 236px;
    border-radius: 40% 40% 50% 50% / 30% 30% 45% 45%;
    background: radial-gradient(circle at 50% 68%, var(--yellow) 0%, #f6d628 42%, rgba(246,214,40,0.35) 66%, rgba(240,240,240,0) 82%);
  }
  .shelf {
    position: absolute; left: 0; top: 588px; width: 512px; height: 39px;
    background: linear-gradient(var(--shelf) 0 78%, var(--shelf-dark) 78% 100%);
  }
  .workbench-art {
    position: absolute; left: 252px; top: 350px; width: 260px; height: 268px;
    border-radius: 60px 0 0 14px;
    background: linear-gradient(180deg, rgba(235,235,235,0) 0%, rgba(226,190,170,0.55) 38%, #d21010 62%, #bc0000 100%);
  }
  .plug-art {
    position: absolute; left: 124px; top: 518px; width: 128px; height: 72px;
    border-radius: 36px;
    background: radial-gradient(ellipse at 45% 50%, rgba(30,30,30,0.75) 0%, rgba(30,30,30,0.35) 55%, rgba(30,30,30,0) 100%);
  }

  .skills { position: absolute; left: 30px; top: 289px; list-style: none; }
  .skills li {
    position: relative; width: 155px; height: 27px; margin-bottom: 3.4px;
    display: flex; align-items: center; border-radius: 14px;
    font-weight: 600; font-size: 21px; color: var(--ink); white-space: nowrap;
  }
  .skills li:nth-child(odd) { background: linear-gradient(90deg, #d4d4d4 0%, #e2e2e2 60%, rgba(230,230,230,0) 100%); }
  .skills .tick { width: 18px; height: 18px; margin: 0 15px 0 5px; flex: none; }

  .apply { position: absolute; left: 0; bottom: 0; width: 100%; text-align: center; }
  .poster--light .apply { height: 97px; background: var(--band-dark); }
  .apply__label {
    display: inline-block; font-family: "Roboto", sans-serif; font-weight: 400;
    border-radius: 7px; line-height: 1;
  }
  .poster--light .apply__label {
    margin-top: 12px; width: 154px; padding: 5px 0;
    border: 1.5px solid var(--yellow); color: var(--yellow); font-size: 15px;
  }
  .poster--light .apply__mail {
    margin-top: 4px; font-weight: 700; font-size: 25px; color: var(--white); letter-spacing: -0.6px; white-space: nowrap;
  }

  /* ---------- Dark poster ---------- */
  .poster--dark {
    left: 621px;
    background: radial-gradient(ellipse at 50% 60%, #1a1a44 0%, var(--navy) 45%, var(--navy-deep) 100%);
    text-align: center;
  }
  .poster--dark .kicker {
    position: absolute; left: 0; width: 100%; top: 31px;
    font-family: "Oswald", sans-serif; font-weight: 400; font-size: 43px; line-height: 1; color: var(--white);
  }
  .poster--dark .headline {
    position: absolute; left: 0; width: 100%;
    font-family: "Bebas Neue", sans-serif; line-height: 1; color: var(--red);
  }
  .poster--dark .headline--power { top: 78px; font-size: 116px; letter-spacing: 1px; }
  .poster--dark .headline--workers { top: 168px; font-size: 116px; letter-spacing: 2.5px; }

  .lamp-photo {
    position: absolute; left: 163px; top: 300px; width: 183px; height: 334px;
    border-radius: 50% 50% 30% 30% / 40% 40% 20% 20%;
    background: radial-gradient(circle at 50% 42%, #ffe27a 0%, #f59a1d 18%, #9b3f12 38%, #1e1c3a 65%, rgba(11,11,44,0) 80%);
  }
  .flow { position: absolute; left: 0; top: 0; width: 512px; height: 724px; }
  .term {
    position: absolute; font-family: "Oswald", sans-serif; font-weight: 400; font-size: 22px;
    line-height: 1; color: var(--amber); transform: translateY(-50%);
  }
  .poster--dark .apply { height: 80px; }
  .poster--dark .apply__label {
    margin-top: 4px; width: 120px; padding: 3px 0;
    border: 1.2px solid var(--red); color: var(--red); font-size: 12px; font-weight: 300;
  }
  .poster--dark .apply__mail {
    margin-top: 12px; font-weight: 600; font-size: 17px; color: var(--white); letter-spacing: 2.6px; white-space: nowrap;
  }
</style>
</head>
<body>

<!-- Illustrated variant -->
<section class="poster poster--light">
  <div class="bulb-art" role="img" aria-label="Illustration einer hängenden gelben Glühbirne mit Lichtstrahlen"></div>
  <p class="kicker">WIR SUCHEN SIE !</p>
  <h1 class="headline headline--power">POWER</h1>
  <h1 class="headline headline--workers">WORKERS</h1>

  <ul class="skills">
    <li><svg class="tick" viewBox="0 0 20 20"><circle cx="10" cy="10" r="8.5" fill="none" stroke="var(--red)" stroke-width="2"/><path d="M6 10.3l2.8 2.8L14 7.8" fill="none" stroke="var(--red)" stroke-width="2" stroke-linecap="round" stroke-linejoin="round"/></svg>STROM</li>
    <li><svg class="tick" viewBox="0 0 20 20"><circle cx="10" cy="10" r="8.5" fill="none" stroke="var(--red)" stroke-width="2"/><path d="M6 10.3l2.8 2.8L14 7.8" fill="none" stroke="var(--red)" stroke-width="2" stroke-linecap="round" stroke-linejoin="round"/></svg>VOLT</li>
    <li><svg class="tick" viewBox="0 0 20 20"><circle cx="10" cy="10" r="8.5" fill="none" stroke="var(--red)" stroke-width="2"/><path d="M6 10.3l2.8 2.8L14 7.8" fill="none" stroke="var(--red)" stroke-width="2" stroke-linecap="round" stroke-linejoin="round"/></svg>WATT</li>
    <li><svg class="tick" viewBox="0 0 20 20"><circle cx="10" cy="10" r="8.5" fill="none" stroke="var(--red)" stroke-width="2"/><path d="M6 10.3l2.8 2.8L14 7.8" fill="none" stroke="var(--red)" stroke-width="2" stroke-linecap="round" stroke-linejoin="round"/></svg>AMPERE</li>
    <li><svg class="tick" viewBox="0 0 20 20"><circle cx="10" cy="10" r="8.5" fill="none" stroke="var(--red)" stroke-width="2"/><path d="M6 10.3l2.8 2.8L14 7.8" fill="none" stroke="var(--red)" stroke-width="2" stroke-linecap="round" stroke-linejoin="round"/></svg>OHM</li>
    <li><svg class="tick" viewBox="0 0 20 20"><circle cx="10" cy="10" r="8.5" fill="none" stroke="var(--red)" stroke-width="2"/><path d="M6 10.3l2.8 2.8L14 7.8" fill="none" stroke="var(--red)" stroke-width="2" stroke-linecap="round" stroke-linejoin="round"/></svg>SPANNUNG</li>
    <li><svg class="tick" viewBox="0 0 20 20"><circle cx="10" cy="10" r="8.5" fill="none" stroke="var(--red)" stroke-width="2"/><path d="M6 10.3l2.8 2.8L14 7.8" fill="none" stroke="var(--red)" stroke-width="2" stroke-linecap="round" stroke-linejoin="round"/></svg>LEISTUNG</li>
  </ul>

  <div class="shelf"></div>
  <div class="workbench-art" role="img" aria-label="Illustration einer Hand mit Schraubenzieher über einem roten Werkzeugkoffer"></div>
  <div class="plug-art" role="img" aria-label="Illustration eines schwarzen Netzsteckers mit Kabel"></div>

  <footer class="apply">
    <span class="apply__label">BEWERBUNG AN :</span>
    <p class="apply__mail">PERSONAL@ELEKTRO-BRANDT.DE</p>
  </footer>
</section>

<!-- Photographic variant -->
<section class="poster poster--dark">
  <p class="kicker">WIR SUCHEN SIE !</p>
  <h1 class="headline headline--power">POWER</h1>
  <h1 class="headline headline--workers">WORKERS</h1>

  <div class="lamp-photo" role="img" aria-label="Foto einer leuchtenden Glühbirne mit glühendem Glühfaden vor dunklem Hintergrund"></div>

  <svg class="flow" viewBox="0 0 512 724" aria-hidden="true">
    <defs>
      <marker id="head" viewBox="0 0 10 10" refX="8" refY="5" markerWidth="7" markerHeight="7" orient="auto-start-reverse">
        <path d="M1 1L8 5L1 9" fill="none" stroke="var(--arrow-grey)" stroke-width="1.6" stroke-linecap="round"/>
      </marker>
    </defs>
    <g fill="none" stroke="var(--arrow-grey)" stroke-width="1.4" stroke-linecap="round" marker-end="url(#head)">
      <path d="M176 327 Q160 307 134 307"/>
      <path d="M345 327 Q360 307 387 307"/>
      <path d="M148 396 Q132 409 106 409"/>
      <path d="M351 443 Q374 446 396 438"/>
      <path d="M163 470 Q160 484 121 493"/>
      <path d="M186 526 Q164 532 153 556"/>
      <path d="M321 532 Q350 526 364 544"/>
    </g>
  </svg>

  <span class="term" style="left:68px; top:309px;">STROM</span>
  <span class="term" style="left:405px; top:311px;">OHM</span>
  <span class="term" style="left:34px; top:407px;">VOLT</span>
  <span class="term" style="left:398px; top:417px;">SPANNUNG</span>
  <span class="term" style="left:40px; top:506px;">WATT</span>
  <span class="term" style="left:372px; top:560px;">LEISTUNG</span>
  <span class="term" style="left:104px; top:583px;">AMPERE</span>

  <footer class="apply">
    <span class="apply__label">BEWERBUNG AN :</span>
    <p class="apply__mail">PERSONAL@ELEKTRO-BRANDT.DE</p>
  </footer>
</section>

</body>
</html>
```